Business Card Design Project

I want a design for my business cards based on an excisting logo design.

Target Market(s)

Marketeers, PR-peeps, CEO's, decisionmakers, entrepreneurs

Industry/Entity Type

Business

Requirements
Nice to have
• Some visual interest on the back too
Should not have
• Sarif on the font

```html
<!DOCTYPE html>
<html lang="nl">
<head>
<meta charset="utf-8">
<title>VerdeVox visitekaartjes</title>
<link rel="stylesheet" href="https://fonts.googleapis.com/css2?family=Open+Sans:wght@400;600;700&display=swap">
<style>
  :root {
    --backdrop: #e4e4e4;
    --card: #ffffff;
    --card-fade: #dcdcdc;
    --green-bright: #8dc63f;
    --green-deep: #0f8a3c;
    --grey-text: #6d6d6d;
    --grey-dark: #555555;
  }
  html, body {
    margin: 0;
    padding: 0;
    width: 1200px;
    height: 1121px;
    overflow: hidden;
    background: var(--backdrop);
    font-family: "Open Sans", Arial, sans-serif;
  }
  .stage {
    position: relative;
    width: 1200px;
    height: 1121px;
  }
  .card {
    position: absolute;
    top: 170px;
    width: 440px;
    height: 770px;
    background: linear-gradient(to bottom, var(--card) 0%, var(--card) 45%, var(--card-fade) 100%);
    box-shadow: 0 6px 18px rgba(0,0,0,0.18);
  }
  .card-front { left: 130px; }
  .card-back { left: 630px; }

  .brand {
    display: flex;
    align-items: center;
    gap: 14px;
  }
  .brand-dot {
    border-radius: 50%;
    background: var(--green-bright);
    flex: none;
  }
  .brand-name {
    color: var(--grey-text);
    font-weight: 400;
    letter-spacing: 0.06em;
  }

  .front-brand {
    position: absolute;
    left: 48px;
    top: 150px;
  }
  .front-brand .brand-dot { width: 44px; height: 44px; }
  .front-brand .brand-name { font-size: 34px; }
  .tagline {
    position: absolute;
    left: 48px;
    top: 206px;
    margin: 0;
    font-size: 10.5px;
    color: var(--grey-text);
  }

  .person {
    position: absolute;
    left: 48px;
    bottom: 70px;
  }
  .person-name {
    margin: 0 0 10px;
    font-size: 33px;
    font-weight: 700;
    color: var(--green-deep);
    letter-spacing: 0.01em;
  }
  .contact-group {
    list-style: none;
    margin: 0 0 16px;
    padding: 0;
  }
  .contact-group li {
    display: flex;
    align-items: flex-start;
    gap: 10px;
    font-size: 19px;
    line-height: 26px;
    color: var(--grey-dark);
  }
  .icon {
    width: 20px;
    height: 20px;
    margin-top: 3px;
    flex: none;
  }
  .icon-spacer { width: 20px; flex: none; }

  .back-brand {
    position: absolute;
    left: 0;
    right: 0;
    top: 250px;
    flex-direction: column;
    gap: 40px;
  }
  .back-brand .brand-dot { width: 170px; height: 170px; }
  .back-brand .brand-name { font-size: 48px; }
</style>
</head>
<body>
<main class="stage">

  <section class="card card-front" aria-label="Voorkant visitekaartje">
    <div class="brand front-brand">
      <span class="brand-dot"></span>
      <span class="brand-name">VerdeVox</span>
    </div>
    <p class="tagline">Systemisch en strategisch PR-, marketing- en communicatieadvies</p>

    <div class="person">
      <h1 class="person-name">LOTTE VERHOEF</h1>
      <ul class="contact-group">
        <li>
          <svg class="icon" viewBox="0 0 20 20"><rect width="20" height="20" fill="var(--green-bright)"/><rect x="4" y="6" width="12" height="8" fill="none" stroke="#fff" stroke-width="1.5"/><path d="M4 6 L10 11 L16 6" fill="none" stroke="#fff" stroke-width="1.5"/></svg>
          lotte.verhoef@verdevox.nl
        </li>
        <li>
          <svg class="icon" viewBox="0 0 20 20"><rect width="20" height="20" fill="var(--green-bright)"/><rect x="7" y="3.5" width="6" height="13" rx="1" fill="none" stroke="#fff" stroke-width="1.5"/><circle cx="10" cy="14" r="0.9" fill="#fff"/></svg>
          +31(0)6 12345678
        </li>
      </ul>
      <ul class="contact-group">
        <li>
          <svg class="icon" viewBox="0 0 20 20"><rect width="20" height="20" fill="var(--green-bright)"/><path d="M4 10 L10 4.5 L16 10 M6 9 V15.5 H14 V9" fill="none" stroke="#fff" stroke-width="1.5"/></svg>
          Lindelaan 12
        </li>
        <li><span class="icon-spacer"></span>6701 AB Veldhoven</li>
      </ul>
      <ul class="contact-group">
        <li>
          <svg class="icon" viewBox="0 0 20 20"><rect width="20" height="20" fill="var(--green-bright)"/><rect x="4" y="4.5" width="12" height="8.5" fill="none" stroke="#fff" stroke-width="1.5"/><path d="M7 16 H13 M10 13 V16" stroke="#fff" stroke-width="1.5"/></svg>
          verdevox.nl
        </li>
        <li>
          <svg class="icon" viewBox="0 0 20 20"><rect width="20" height="20" fill="var(--green-bright)"/></svg>
          social.example/_verdevox
        </li>
        <li>
          <svg class="icon" viewBox="0 0 20 20"><rect width="20" height="20" fill="var(--green-bright)"/></svg>
          social.example/verdevox
        </li>
      </ul>
    </div>
  </section>

  <section class="card card-back" aria-label="Achterkant visitekaartje">
    <div class="brand back-brand">
      <span class="brand-dot"></span>
      <span class="brand-name">VerdeVox</span>
    </div>
  </section>

</main>
</body>
</html>
```